Startup internet service provider needs a good facebook ad

Looking for a catchy facebook ad to launch our internet service in Parker, Colorado. Short video or slideshow preferred, still pictures are okay.

https://www.facebook.com/BrimfoxNetworks

www.brimfox-networks.example

Target Market(s)

Parker Colorado

Colors
add136
0255a3

```html
<!DOCTYPE html>
<html lang="en">
<head>
<meta charset="utf-8">
<title>Brimfox Networks – Fast and Reliable Internet</title>
<link rel="stylesheet" href="https://fonts.googleapis.com/css2?family=Poppins:wght@400;500;700;800&display=swap">
<style>
  :root {
    --brand-green: #add136;
    --brand-blue: #0255a3;
    --ink: #1c1c1c;
    --paper: #ffffff;
    --backdrop: #ececec;
  }
  * { box-sizing: border-box; margin: 0; padding: 0; }
  html, body {
    width: 1200px; height: 1200px; overflow: hidden;
    background: var(--backdrop);
    font-family: "Poppins", sans-serif;
  }
  .ad-banner {
    position: absolute; left: 30px; top: 302px;
    width: 1140px; height: 596px;
    background: var(--paper);
    overflow: hidden;
  }
  .ad-shapes { position: absolute; inset: 0; width: 100%; height: 100%; }
  .brand {
    position: absolute; left: 32px; top: 27px; height: 55px;
    display: flex; align-items: center; gap: 10px;
  }
  .brand-dot { width: 52px; height: 52px; border-radius: 50%; background: var(--brand-blue); }
  .brand-name { font-size: 27px; font-weight: 400; color: var(--brand-blue); letter-spacing: 0.2px; }
  .headline-rule {
    position: absolute; left: 32px; top: 117px; width: 2px; height: 93px;
    background: var(--brand-green);
  }
  .headline {
    position: absolute; left: 46px; top: 108px;
    font-size: 58px; font-weight: 700; line-height: 1; color: var(--brand-green);
    letter-spacing: -0.5px;
  }
  .subhead {
    position: absolute; left: 46px; top: 165px; width: 520px;
    font-size: 22.5px; font-weight: 400; line-height: 26px; color: var(--brand-blue);
  }
  .features {
    position: absolute; left: 32px; top: 230px;
    list-style: none; font-size: 20px; line-height: 28.3px; color: var(--ink);
  }
  .features li::before { content: "– "; }
  .web-link {
    position: absolute; left: 50px; top: 482px; height: 24px;
    display: flex; align-items: center; gap: 16px;
    font-size: 14.5px; font-weight: 500; color: var(--paper); text-transform: uppercase;
    letter-spacing: 0.2px;
  }
  .phone-line {
    position: absolute; left: 32px; top: 522px; height: 64px;
    display: flex; align-items: center; gap: 24px;
  }
  .phone-number { font-size: 53px; font-weight: 800; color: #111; letter-spacing: 0.5px; line-height: 1; }
</style>
</head>
<body>
<main class="ad-banner">
  <svg class="ad-shapes" viewBox="0 0 1750 915" preserveAspectRatio="none" aria-hidden="false">
    <defs>
      <radialGradient id="photo-tones" cx="50%" cy="45%" r="60%">
        <stop offset="0%" stop-color="#d9cfc2"/>
        <stop offset="55%" stop-color="#a99a86"/>
        <stop offset="100%" stop-color="#6f6a5f"/>
      </radialGradient>
    </defs>
    <!-- green panels -->
    <polygon points="1254,0 1750,0 1750,20 1262,915 900,915 900,700" fill="var(--brand-green)"/>
    <path d="M0,783 L830,783 C880,783 900,700 960,680 L1100,680 L1100,915 L0,915 Z" fill="var(--brand-green)"/>
    <!-- blue corner -->
    <polygon points="1750,52 1750,915 1284,915" fill="var(--brand-blue)"/>
    <!-- website band -->
    <path d="M0,736 L745,736 C778,736 790,760 800,783 L0,783 Z" fill="var(--brand-blue)"/>
    <!-- photo circle -->
    <circle cx="1254" cy="466" r="374" fill="var(--paper)"/>
    <circle cx="1254" cy="466" r="360" fill="url(#photo-tones)" role="img"
      aria-label="Photo: a family of four on a sofa using a tablet, phone and laptop in front of bookshelves"/>
  </svg>

  <div class="brand">
    <span class="brand-dot"></span>
    <span class="brand-name">Brimfox Networks</span>
  </div>

  <span class="headline-rule"></span>
  <h1 class="headline">Fast and Reliable</h1>
  <p class="subhead">internet service designed and catered to meet your needs</p>

  <ul class="features">
    <li>Fast and reliable internet service</li>
    <li>Real customer support</li>
    <li>Less buffering while streaming</li>
    <li>Fast web browsing</li>
    <li>Gaming without the lag</li>
    <li>Wall to wall WiFi coverage</li>
    <li>No introductory charges, one constant rate</li>
    <li>Simple and easy to read bills</li>
  </ul>

  <div class="web-link">
    <svg width="16" height="16" viewBox="0 0 16 16" aria-hidden="true">
      <circle cx="8" cy="8" r="7" fill="none" stroke="#fff" stroke-width="1.6"/>
      <ellipse cx="8" cy="8" rx="3" ry="7" fill="none" stroke="#fff" stroke-width="1.3"/>
      <line x1="1" y1="8" x2="15" y2="8" stroke="#fff" stroke-width="1.3"/>
      <line x1="2.5" y1="4.5" x2="13.5" y2="4.5" stroke="#fff" stroke-width="1.1"/>
      <line x1="2.5" y1="11.5" x2="13.5" y2="11.5" stroke="#fff" stroke-width="1.1"/>
    </svg>
    <span>www.brimfox-networks.example</span>
  </div>

  <div class="phone-line">
    <svg width="38" height="38" viewBox="0 0 24 24" aria-hidden="true">
      <path d="M6.6 10.8a15.1 15.1 0 0 0 6.6 6.6l2.2-2.2a1 1 0 0 1 1-.25 11.4 11.4 0 0 0 3.6.57 1 1 0 0 1 1 1V20a1 1 0 0 1-1 1A17 17 0 0 1 3 4a1 1 0 0 1 1-1h3.5a1 1 0 0 1 1 1c0 1.25.2 2.45.57 3.57a1 1 0 0 1-.25 1z" fill="#111"/>
      <path d="M14.5 2.5a7 7 0 0 1 7 7M14.5 6a3.5 3.5 0 0 1 3.5 3.5" fill="none" stroke="#111" stroke-width="1.8" stroke-linecap="round"/>
    </svg>
    <span class="phone-number">844-555-0187</span>
  </div>
</main>
</body>
</html>
```